Skincare Cleanser Bottle Label

New product launch of a mint facial cleanser.
Brand is called Dorvella.
Product will be called Lumora.
Looking for a label design that can be printed using silk screening.
High gloss white plastic bottle. 8oz. White push pump top.
Clinical skincare brand, professional image, sold in medical spas.

Target Market(s)

Women Age 20-65

Industry/Entity Type

Health And Wellness

Font styles to use
Serif
Sans Serif

Requirements
Must have
• Dorvella brand name in the orignal font.
Should not have
• Multiple colours.

```html
<!DOCTYPE html>
<html lang="en">
<head>
<meta charset="utf-8">
<title>Lumora Mint Facial Wash – Dorvella Label</title>
<link rel="stylesheet" href="https://fonts.googleapis.com/css2?family=Playfair+Display:ital,wght@1,600&family=Didact+Gothic&family=Open+Sans:wght@700&display=swap">
<style>
  :root {
    --backdrop: #d3d0d6;
    --label: #ffffff;
    --label-edge: #e4e4e6;
    --leaf-green: #0f9a48;
    --lime: #8dc63f;
    --ink: #2b2b2b;
    --alert-red: #c1272d;
    --mint-light: #9fd46a;
    --mint-dark: #3f8f2a;
  }
  html, body {
    margin: 0;
    padding: 0;
    width: 1200px;
    height: 1143px;
    overflow: hidden;
    background: var(--backdrop);
  }
  .label {
    position: absolute;
    left: 398px;
    top: 60px;
    width: 403px;
    height: 1023px;
    display: block;
  }
  .label-sheet { fill: var(--label); stroke: var(--label-edge); stroke-width: 1; }
  .product-name {
    font-family: "Playfair Display", Georgia, serif;
    font-style: italic;
    font-weight: 600;
    font-size: 96px;
    fill: var(--leaf-green);
  }
  .variant-band { fill: var(--leaf-green); }
  .variant-text, .claim-text, .feature-text {
    font-family: "Open Sans", Arial, sans-serif;
    font-weight: 700;
  }
  .variant-text { font-size: 19px; fill: var(--label); letter-spacing: 0.5px; }
  .brand-name {
    font-family: "Didact Gothic", "Century Gothic", sans-serif;
    font-size: 92px;
    fill: var(--ink);
  }
  .descriptor {
    font-family: "Didact Gothic", "Century Gothic", sans-serif;
    font-size: 50px;
    fill: var(--lime);
  }
  .herb-frame { fill: none; stroke: var(--lime); stroke-width: 2.5; }
  .claim-band { fill: var(--alert-red); }
  .claim-text { font-size: 12.5px; fill: var(--label); }
  .feature-bullet { fill: var(--lime); }
  .feature-text { font-size: 13.5px; fill: var(--ink); letter-spacing: 0.4px; }
  .social-mark { fill: var(--ink); }
  .social-handle {
    font-family: "Didact Gothic", "Century Gothic", sans-serif;
    font-size: 17px;
    fill: var(--ink);
  }
  .net-volume {
    font-family: "Didact Gothic", "Century Gothic", sans-serif;
    font-size: 27px;
    fill: var(--ink);
  }
  .formula-seal { fill: var(--leaf-green); }
  .formula-seal-ring { fill: none; stroke: var(--label); stroke-width: 2; }
</style>
</head>
<body>
<svg class="label" viewBox="0 0 403 1023" xmlns="http://www.w3.org/2000/svg">
  <defs>
    <linearGradient id="mintLeaves" x1="0" y1="0" x2="1" y2="1">
      <stop offset="0" stop-color="var(--mint-light)"/>
      <stop offset="1" stop-color="var(--mint-dark)"/>
    </linearGradient>
  </defs>

  <rect class="label-sheet" x="0" y="0" width="403" height="1023"/>

  <text class="product-name" x="22" y="190">Lumora</text>

  <g class="variant-tag">
    <rect class="variant-band" x="152" y="217" width="231" height="42"/>
    <text class="variant-text" x="267" y="245" text-anchor="middle">MINT FACIAL WASH</text>
  </g>

  <text class="brand-name" transform="translate(101 891) rotate(-90)" textLength="520" lengthAdjust="spacingAndGlyphs">dorvella</text>
  <text class="descriptor" transform="translate(160 891) rotate(-90)" textLength="510" lengthAdjust="spacingAndGlyphs">mint facial cleanser</text>

  <g class="herb-emblem">
    <polygon class="herb-frame" points="260,466 348,516 348,616 260,666 172,616 172,516"/>
    <ellipse cx="260" cy="566" rx="58" ry="36" fill="url(#mintLeaves)" role="img" aria-label="Fresh mint leaves"/>
  </g>

  <g class="claim">
    <rect class="claim-band" x="170" y="700" width="213" height="58"/>
    <text class="claim-text" x="185" y="724">TRANSFORM THE APPEARANCE</text>
    <text class="claim-text" x="185" y="744">AND HEALTH OF YOUR SKIN</text>
  </g>

  <g class="features">
    <rect class="feature-bullet" x="170" y="799" width="10" height="10"/>
    <text class="feature-text" x="190" y="809">PARABEN FREE</text>
    <rect class="feature-bullet" x="170" y="821" width="10" height="10"/>
    <text class="feature-text" x="190" y="831">NO PRESERVATIVES</text>
    <rect class="feature-bullet" x="170" y="843" width="10" height="10"/>
    <text class="feature-text" x="190" y="853">NO FILLERS</text>
  </g>

  <g class="social">
    <rect class="social-mark" x="31" y="948" width="14" height="14"/>
    <text class="social-handle" x="52" y="961">@dorvella</text>
  </g>

  <text class="net-volume" x="209" y="964">8 oz</text>

  <g class="formula-badge">
    <circle class="formula-seal" cx="326" cy="930" r="36"/>
    <circle class="formula-seal-ring" cx="326" cy="930" r="28"/>
  </g>
</svg>
</body>
</html>
```